tallkettle.example - youth/backpackers Adventure Travel contact site

Landing Page: Logo, @RidgelineRoamerCrew, Australia | New Zealand | Fiji | South East Asia, Start Button, a Rotating carousel of supplier logos, ©Tall Kettle Travel, Terms and Conditions link, Contact Us page link, social media/contact icons.
Start Button: Takes you to destinations selection Map - Hover over effect with selectable Countries, states, regions, and next & back buttons.
Next Button: Takes you to Activities - Selectable Buttons for Sky Diving, Sailing, Whitewater Rafting, Bungee jumping, camping, hiking, Surfing, Jet Boating, kayaking, canyoning, National Parks, Scuba Diving, Snorkeling and beaches etc., Tandem Hand gliding, with a typable "Have we missed anything you want to experience" area and back and next buttons.
Next Button: Takes you to extras - Selectable buttons for Bus Passes, Accommodation, Car Hire, Camper Hire and back and next buttons.
Next Button: Takes you to enter customer details: Name, Age, Phone, Email, How did you hear about us, Dietary requirement, start & end date, start & end location, Number of Travellers, Budget, anything else area, Submit for your custom adventure button. - All this information then gets emailed.

Target Market(s)

Backpacker/youth adventure travel

Industry/Entity Type

Travel Agent

Coding

Coded - Design and coding required

Number of Pages Required

3 page

Colors

Designer to choose colors to be used in the design.

Requirements
Must have
• Somewhere to be automatically synced Instagram profile pictures and videos.
• Full screen, scalable to any device size - 65% of our users use mobile devices.
• Wordpress
Nice to have
• Easy to add and remove selectable buttons
• If you can think of any special feature to add ;)
Should not have
• Basic contact form look

```html
<!DOCTYPE html>
<html lang="en">
<head>
<meta charset="utf-8">
<title>Tall Kettle Travel – Our Destination</title>
<link rel="stylesheet" href="https://fonts.googleapis.com/css2?family=Jost:wght@400;500;600&display=swap">
<style>
  :root {
    --coral: #fa5245;
    --navy: #2f3b55;
    --cream: #f9e0c8;
    --white: #ffffff;
    --black: #050507;
    --line: rgba(255,255,255,0.75);
  }
  * { box-sizing: border-box; margin: 0; padding: 0; }
  html, body { width: 1200px; height: 918px; overflow: hidden; }
  body { font-family: "Jost", "Futura", sans-serif; background: var(--navy); position: relative; }

  .map-panel {
    position: absolute; left: 0; top: 0; width: 514px; height: 825px;
    background: var(--coral);
    box-shadow: 6px 0 10px rgba(0,0,0,0.25);
    z-index: 2;
  }
  .menu-toggle { position: absolute; left: 50px; top: 47px; width: 20px; height: 18px; }
  .menu-toggle span {
    display: block; height: 3.5px; border-radius: 2px; background: var(--white); margin-bottom: 3.5px;
  }
  .region-map {
    position: absolute; left: 26px; top: 140px; width: 446px; height: 480px;
    border-radius: 40% 30% 35% 45%;
    background: linear-gradient(160deg, var(--cream) 0%, var(--cream) 48%, var(--navy) 72%, var(--navy) 100%);
    opacity: 0.95;
  }

  .content-panel { position: absolute; left: 514px; top: 0; width: 686px; height: 825px; }
  .brand {
    position: absolute; left: 38px; top: 40px;
    display: flex; align-items: center; gap: 8px;
    color: var(--coral); font-weight: 600; font-size: 17px; letter-spacing: 0.5px;
  }
  .brand-dot { width: 14px; height: 14px; border-radius: 50%; background: var(--coral); }
  .social { position: absolute; right: 50px; top: 48px; display: flex; gap: 20px; align-items: center; }
  .social-dot { width: 20px; height: 20px; border-radius: 50%; background: var(--white); }
  .social svg { display: block; }

  .page-title {
    position: absolute; left: 0; width: 686px; top: 145px; text-align: center;
    color: var(--white); font-weight: 500; font-size: 48px; letter-spacing: 2px;
  }
  .title-rule { position: absolute; left: 177px; top: 227px; width: 303px; height: 1px; background: var(--line); }
  .country {
    position: absolute; left: 0; width: 686px; top: 276px; text-align: center;
    color: var(--coral); font-weight: 500; font-size: 24px; letter-spacing: 1px;
  }
  .country-intro {
    position: absolute; left: 97px; top: 336px; width: 467px;
    color: var(--white); font-size: 13.6px; line-height: 19.5px;
    text-align: justify; text-align-last: center;
  }

  .filter-band {
    position: absolute; left: 33px; top: 558px; width: 591px; height: 110px;
    border-top: 1px solid var(--line); border-bottom: 1px solid var(--line);
  }
  .select {
    position: absolute; top: 39px; width: 222px; height: 33px; background: var(--white);
    color: var(--navy); font-weight: 500; font-size: 12.5px; padding-left: 12px;
    display: flex; align-items: center; justify-content: space-between; padding-right: 10px;
  }
  .select-state { left: 25px; }
  .select-region { left: 346px; }

  .step-nav { position: absolute; left: 214px; top: 747px; display: flex; gap: 16px; }
  .btn {
    width: 121px; height: 35px; border-radius: 18px;
    display: flex; align-items: center; justify-content: center; gap: 22px;
    font-weight: 600; font-size: 12.5px;
  }
  .btn-back { background: var(--cream); color: var(--coral); }
  .btn-next { background: var(--coral); color: var(--white); }

  .site-footer {
    position: absolute; left: 0; top: 825px; width: 1200px; height: 93px; background: var(--black);
    color: var(--white); text-align: center;
  }
  .copyright { margin-top: 17px; font-size: 13.5px; letter-spacing: 0.6px; text-transform: uppercase; }
  .footer-links { margin-top: 14px; display: flex; justify-content: center; font-size: 10.5px; letter-spacing: 0.4px; }
  .footer-links a { color: var(--white); text-decoration: none; padding: 0 10px; border-left: 1px solid var(--white); line-height: 14px; }
  .footer-links a:first-child { border-left: none; }
</style>
</head>
<body>
  <aside class="map-panel">
    <div class="menu-toggle"><span></span><span></span><span></span></div>
    <div class="region-map" role="img" aria-label="Map of Asia and Oceania with Australia highlighted under a pointer cursor"></div>
  </aside>

  <main class="content-panel">
    <div class="brand"><span class="brand-dot"></span>Tall Kettle Travel</div>
    <nav class="social">
      <span class="social-dot"></span>
      <span class="social-dot"></span>
      <span class="social-dot"></span>
      <svg width="23" height="17" viewBox="0 0 23 17" aria-label="Email">
        <rect x="0" y="0" width="23" height="17" rx="2" fill="#fff"/>
        <path d="M1 2 L11.5 10 L22 2" fill="none" stroke="#2f3b55" stroke-width="1.6"/>
      </svg>
    </nav>

    <h1 class="page-title">OUR DESTINATION</h1>
    <div class="title-rule"></div>
    <h2 class="country">AUSTRALIA</h2>
    <p class="country-intro">Lorem ipsum dolor sit amet, consectetur adipiscing elit. Suspendisse suscipit leo a quam auctor, egestas posuere ipsum lobortis. Nunc vestibulum ligula vel orci bibendum euismod. Proin laoreet purus lectus, non finibus erat scelerisque ac. Aenean a urna ante. Cras gravida at ipsum sed pulvinar. Maecenas quis libero ipsum.</p>

    <div class="filter-band">
      <div class="select select-state">STATE
        <svg width="8" height="14" viewBox="0 0 8 14"><path d="M1 5 L4 2 L7 5 M1 9 L4 12 L7 9" fill="none" stroke="#2f3b55" stroke-width="1.2"/></svg>
      </div>
      <div class="select select-region">REGION
        <svg width="8" height="14" viewBox="0 0 8 14"><path d="M1 5 L4 2 L7 5 M1 9 L4 12 L7 9" fill="none" stroke="#2f3b55" stroke-width="1.2"/></svg>
      </div>
    </div>

    <div class="step-nav">
      <div class="btn btn-back">
        <svg width="6" height="10" viewBox="0 0 6 10"><path d="M5 1 L1 5 L5 9" fill="none" stroke="#fa5245" stroke-width="1.8"/></svg>
        BACK
      </div>
      <div class="btn btn-next">
        NEXT
        <svg width="6" height="10" viewBox="0 0 6 10"><path d="M1 1 L5 5 L1 9" fill="none" stroke="#fff" stroke-width="1.8"/></svg>
      </div>
    </div>
  </main>

  <footer class="site-footer">
    <p class="copyright">© Copyright 2017 @RidgelineRoamerCrew</p>
    <div class="footer-links">
      <a href="#">CONTACT US</a>
      <a href="#">TERMS AND CONDITIONS</a>
      <a href="#">PRIVACY POLICY</a>
    </div>
  </footer>
</body>
</html>
```